B2B EDM Banner Design- Specialist Tech Company

We need a new top-of-email banner for our EDM campaigns for Brelmont Digest (www.brelmontdigest.example
). This banner will sit at the top of every email and must immediately signal the brand, look modern and professional, and be visually aligned with the tech/IT audience.
Size of the banner: Around 728x90 - it must fit at the top of an email blast.
Purpose of the Banner
Establish a strong, recognizable brand identity across all Brelmont Digest EDMs
visually consistent with existing banners created for other brands (see reference examples provided)
Communicate Brelmont Digest’s value proposition at a glance
Brand Name
Brelmont Digest
Tagline (must appear in the banner)
“11,322 whitepapers from 726 companies”
Design Requirements
Style & Tone
Modern, clean, and professional
Tech-centric look and feel
High-quality, sleek, and corporate
Eye-catching but not cluttered
Should feel premium and authoritative
Layout & Composition
Full-width banner for email header
Horizontal orientation similar to the StaffLoom and Workforce Paper Vault examples
Include space for the brand name/logo prominently on the left or centered
Integrate the tagline in a readable, secondary position
Optional: a subtle background texture or tech-related abstract pattern (circuitry, network nodes, gradient, etc.)
No busy imagery—should feel clean and trustworthy
Color Palette
Use colors consistent with Brelmont Digest branding from www.brelmontdigest.example
Blues, greys, blacks, and tech-style gradients preferred
Should feel consistent with a B2B IT audience
Typography
Clean, sans-serif fonts (professional/tech-aligned)
Brand name should be bold and prominent
Tagline should be smaller, but still readable on desktop and mobile
Imagery (if used)
Abstract tech shapes, network visuals, geometric patterns, or gradient overlays
Avoid photography of people
Keep imagery subtle so text remains legible
Call-to-Action Button (optional)
None required in this banner (unlike the HR examples)
Banner should remain a pure brand header
Deliverables
Final banner in PNG and JPG formats
2–3 design variations (if possible) for A/B testing
Dimensions optimized for EDM: ~600–700px wide (standard email width), proportionate height

```html
<!DOCTYPE html>
<html lang="en">
<head>
<meta charset="utf-8">
<title>Brelmont Digest – Email Header Banner</title>
<link rel="stylesheet" href="https://fonts.googleapis.com/css2?family=Big+Shoulders+Display:wght@800&family=Dancing+Script:wght@700&family=Montserrat:wght@700;800&display=swap">
<style>
  :root {
    --page-bg: #ebebeb;
    --navy-deep: #050a4a;
    --navy: #0a1466;
    --brand-blue: #1a9ae0;
    --sky-light: #7fd6f7;
    --sky: #1ea2e3;
    --silver-light: #ffffff;
    --silver-dark: #b9b9bf;
    --white: #ffffff;
  }
  * { margin: 0; padding: 0; box-sizing: border-box; }
  html, body {
    width: 1200px;
    height: 269px;
    overflow: hidden;
    background: var(--page-bg);
  }
  .banner {
    position: absolute;
    left: 49px;
    top: 67px;
    width: 1103px;
    height: 136px;
    overflow: hidden;
    box-shadow: 0 6px 10px rgba(0,0,0,0.25);
    background:
      radial-gradient(ellipse 260px 120px at 527px 0, rgba(61,127,214,0.85), rgba(20,60,170,0.35) 55%, transparent 100%),
      radial-gradient(ellipse 420px 160px at 527px 60px, rgba(20,60,180,0.55), transparent 80%),
      linear-gradient(90deg, var(--navy-deep), var(--navy) 50%, var(--navy-deep));
  }
  .brand {
    position: absolute;
    left: 22px;
    top: 40px;
    display: flex;
    align-items: center;
    gap: 12px;
  }
  .brand-mark {
    width: 56px;
    height: 56px;
    border-radius: 50%;
    background: var(--brand-blue);
    flex: none;
  }
  .brand-name {
    font-family: "Montserrat", sans-serif;
    font-weight: 800;
    font-size: 22px;
    line-height: 1;
    color: var(--white);
    text-transform: uppercase;
  }
  .brand-tagline {
    margin-top: 8px;
    padding-top: 5px;
    border-top: 1px solid rgba(26,154,224,0.7);
    font-family: "Montserrat", sans-serif;
    font-weight: 700;
    font-size: 8.5px;
    letter-spacing: 5.1px;
    color: var(--white);
    text-transform: uppercase;
    white-space: nowrap;
  }
  .headline {
    position: absolute;
    left: 349px;
    top: 20px;
    width: 406px;
    height: 64px;
    overflow: visible;
  }
  .headline-text {
    font-family: "Big Shoulders Display", sans-serif;
    font-weight: 800;
    font-size: 76px;
  }
  .subline {
    position: absolute;
    left: 377px;
    top: 80px;
    display: flex;
    align-items: baseline;
    white-space: nowrap;
  }
  .subline-from {
    font-family: "Dancing Script", cursive;
    font-weight: 700;
    font-size: 34px;
    color: var(--white);
    text-shadow: 0 0 6px rgba(127,214,247,0.9);
    margin-right: 2px;
    transform: translateY(8px) rotate(-6deg);
    display: inline-block;
  }
  .subline-count {
    font-family: "Montserrat", sans-serif;
    font-weight: 800;
    font-size: 34px;
    letter-spacing: -0.3px;
    background: linear-gradient(90deg, var(--sky) 0%, var(--sky-light) 100%);
    -webkit-background-clip: text;
    background-clip: text;
    color: transparent;
  }
  .circuit-art {
    position: absolute;
    left: 760px;
    top: 0;
    width: 343px;
    height: 136px;
    background:
      radial-gradient(ellipse 200px 70px at 60% 50%, rgba(31,79,216,0.35), transparent 80%),
      linear-gradient(90deg, transparent, rgba(31,79,216,0.18) 40%, rgba(31,79,216,0.12) 85%, transparent);
  }
</style>
</head>
<body>
  <div class="banner">
    <div class="brand">
      <div class="brand-mark"></div>
      <div class="brand-text">
        <div class="brand-name">Brelmont Digest</div>
        <div class="brand-tagline">For IT Professionals</div>
      </div>
    </div>

    <svg class="headline" viewBox="0 0 406 64" aria-label="11,322 Whitepapers">
      <defs>
        <linearGradient id="silver" x1="0" y1="0" x2="0" y2="1">
          <stop offset="0.2" stop-color="#ffffff"/>
          <stop offset="1" stop-color="#b9b9bf"/>
        </linearGradient>
      </defs>
      <text class="headline-text" x="2" y="61" fill="url(#silver)" textLength="402" lengthAdjust="spacingAndGlyphs">11,322 WHITEPAPERS</text>
    </svg>

    <div class="subline">
      <span class="subline-from">from</span>
      <span class="subline-count">726 COMPANIES</span>
    </div>

    <div class="circuit-art" role="img" aria-label="Abstract blue circuit-board trace lines with glowing nodes"></div>
  </div>
</body>
</html>
```